Fruits and Vegetables distribution company needs a new eye catching website

We need to get our website up to date. Our clients will look at our website to learn about our products and services. Our design needs to be simple yet impactful to make our brand memorable to our visitors. We need to have somewhere to tell our clients about our history, products and services, our team. We can throw in a few fun facts and figures and maybe some testimonials to impress. We have 4 theme colors that we want to incorporate into the design, you can get in touch for the HEX/RGB codes. Please remember that smooth operation of any animations and interactions is very important.

```html
<!DOCTYPE html>
<html lang="en">
<head>
<meta charset="utf-8">
<title>Bustan – Contact</title>
<link href="https://fonts.googleapis.com/css2?family=Marcellus&family=Mulish:wght@400;600&display=swap" rel="stylesheet">
<style>
:root{
  --green:#8dc63f;
  --red:#c4262e;
  --amber:#f5a623;
  --ink:#111111;
  --muted:#555555;
  --panel:#f2f2f2;
  --line:#dddddd;
  --white:#ffffff;
}
*{box-sizing:border-box;margin:0;padding:0}
html,body{width:1044px;height:1200px;overflow:hidden;background:var(--white)}
body{position:relative;font-family:"Mulish",sans-serif;color:var(--ink)}
.abs{position:absolute}
.display{font-family:"Marcellus",serif}

/* header */
.header{left:0;top:0;width:1044px;height:92px;background:var(--white)}
.contact-chip{display:flex;align-items:center;gap:9px;font-size:14px;letter-spacing:.5px;color:#222}
.chip-icon{width:28px;height:28px;border-radius:50%;border:2px solid #f6e4b8;display:flex;align-items:center;justify-content:center}
.social-top{display:flex;gap:8px}
.social-dot{width:26px;height:26px;border-radius:50%;border:2px solid #f6e4b8;display:flex;align-items:center;justify-content:center}
.social-dot span{width:8px;height:8px;border-radius:50%;background:var(--amber)}
.nav{top:60px;font-family:"Marcellus",serif;font-size:12.5px;color:var(--ink);letter-spacing:.3px}
.nav.active{color:var(--green)}
.brand-box{left:462px;top:0;width:117px;height:120px;background:var(--white);z-index:3;display:flex;flex-direction:column;align-items:center;justify-content:center;gap:8px;box-shadow:0 3px 6px rgba(0,0,0,.08)}
.brand-mark{width:22px;height:22px;border-radius:50%;background:var(--red)}
.brand-name{font-family:"Marcellus",serif;font-size:18px;letter-spacing:2px;color:#333}

/* hero */
.hero{left:0;top:92px;width:1044px;height:246px;background:linear-gradient(100deg,#3c6b2a 0%,#b8321f 22%,#6b4a2c 45%,#d8b11c 62%,#5b7f2a 80%,#3a2238 100%)}
.hero-title{left:0;top:198px;width:1044px;text-align:center;font-family:"Marcellus",serif;font-size:25px;color:var(--white);letter-spacing:.3px;text-shadow:0 1px 3px rgba(0,0,0,.4)}

/* breadcrumb */
.crumbs{left:122px;top:346px;display:flex;align-items:center;gap:18px;font-size:10.5px;color:#666}
.crumbs .current{color:var(--green)}
.crumb-rule{left:0;top:368px;width:1044px;height:1px;background:#ececec}

/* section heading */
.section-title{left:0;top:422px;width:1044px;text-align:center;font-family:"Marcellus",serif;font-size:25px}
.divider-line{top:474px;height:1px;width:110px;background:#555}
.divider-dot{left:514px;top:467px;width:14px;height:14px;border-radius:50%;border:1.5px solid #444}

/* form panel */
.panel{left:0;top:513px;width:1044px;height:344px;background:var(--panel)}
.form-title{left:123px;top:540px;font-family:"Marcellus",serif;font-size:17px}
.field{background:var(--white);border:1px solid #e0e0e0;font-size:11.5px;color:#222;padding:8px 8px}
.submit{left:122px;top:797px;width:116px;height:28px;background:var(--green);color:var(--white);font-size:12px;display:flex;align-items:center;justify-content:center}
.map{left:630px;top:513px;width:414px;height:344px;background:linear-gradient(135deg,#e8eee0 0%,#f0ede6 45%,#ece8df 100%)}

/* info card */
.info-card{left:122px;top:888px;width:799px;height:188px;background:var(--white);box-shadow:0 2px 10px rgba(0,0,0,.12)}
.info-col{top:0;height:188px;display:flex;flex-direction:column;align-items:center;padding-top:32px}
.info-icon{width:34px;height:34px;border-radius:50%;background:#f0f0f0;display:flex;align-items:center;justify-content:center}
.info-title{margin-top:10px;font-family:"Marcellus",serif;font-size:17px}
.info-text{margin-top:8px;font-size:10px;line-height:13px;text-align:center;color:#222}
.info-btn{margin-top:10px;width:125px;height:28px;background:var(--green);color:var(--white);font-size:11px;display:flex;align-items:center;justify-content:center}
.col-rule{top:26px;width:1px;height:140px;background:#e6e6e6}

/* footer */
.social-foot{left:462px;top:1108px;display:flex;gap:8px}
.social-foot .social-dot{border-color:#dfe9cf}
.social-foot .social-dot span{background:var(--green)}
.footer-bar{left:0;top:1162px;width:1044px;height:38px;background:var(--red);color:var(--white);font-size:10.5px;display:flex;align-items:center;justify-content:center;gap:5px}
.footer-bar .brand-inline{font-family:"Mulish",sans-serif;letter-spacing:1px}
</style>
</head>
<body>

<header class="abs header">
  <div class="abs contact-chip" style="left:122px;top:10px">
    <div class="chip-icon">
      <svg width="12" height="9" viewBox="0 0 12 9"><rect width="12" height="9" rx="1" fill="#f5a623"/><path d="M0 1 6 5 12 1" stroke="#fff" fill="none" stroke-width="1.2"/></svg>
    </div>
    info@bustanfresh.com
  </div>

  <div class="abs contact-chip" style="left:648px;top:8px">
    <div class="chip-icon">
      <svg width="12" height="12" viewBox="0 0 24 24"><path fill="#f5a623" d="M6.6 10.8a15 15 0 0 0 6.6 6.6l2.2-2.2c.3-.3.7-.4 1-.2 1.1.4 2.3.6 3.6.6.6 0 1 .4 1 1V20c0 .6-.4 1-1 1A17 17 0 0 1 3 4c0-.6.4-1 1-1h3.5c.6 0 1 .4 1 1 0 1.3.2 2.5.6 3.6.1.3 0 .7-.2 1z"/></svg>
    </div>
    123-456-7890
  </div>

  <div class="abs social-top" style="left:800px;top:10px" aria-label="Social links">
    <div class="social-dot"><span></span></div>
    <div class="social-dot"><span></span></div>
    <div class="social-dot"><span></span></div>
    <div class="social-dot"><span></span></div>
  </div>

  <svg class="abs" style="left:123px;top:60px" width="15" height="14" viewBox="0 0 15 14" aria-label="Home"><path d="M7.5 0 15 7h-2v7H9V9H6v5H2V7H0z" fill="#111"/></svg>
  <div class="abs nav" style="left:167px">OUR HISTORY</div>
  <div class="abs nav" style="left:274px">DIVISIONS</div>
  <div class="abs nav" style="left:370px">PRODUCT</div>
  <div class="abs nav" style="left:616px">SERVICES</div>
  <div class="abs nav" style="left:716px">MEDIA COVERAGE</div>
  <div class="abs nav active" style="left:865px">CONTACT</div>

  <div class="abs brand-box">
    <div class="brand-mark"></div>
    <div class="brand-name">BUSTAN</div>
  </div>
</header>

<div class="abs hero" role="img" aria-label="Photo of a wicker basket with tomatoes, yellow peppers, cucumbers, eggplants and garlic"></div>
<h1 class="abs hero-title">WE ARE A FRUITS &amp; VEGETABLES DISTRIBUTION COMPANY</h1>

<nav class="abs crumbs">
  <span>HOME</span>
  <svg width="15" height="8" viewBox="0 0 15 8"><path d="M0 4h13M10 1l3 3-3 3" stroke="#555" fill="none" stroke-width="1"/></svg>
  <span class="current">CONTACT US</span>
</nav>
<div class="abs crumb-rule"></div>

<h2 class="abs section-title">CONTACT US</h2>
<div class="abs divider-line" style="left:396px"></div>
<div class="abs divider-dot"></div>
<div class="abs divider-line" style="left:537px"></div>

<section class="abs panel"></section>
<h3 class="abs form-title">SENT US MESSAGE</h3>
<div class="abs field" style="left:123px;top:587px;width:225px;height:30px">Name</div>
<div class="abs field" style="left:368px;top:587px;width:225px;height:30px">Email</div>
<div class="abs field" style="left:123px;top:630px;width:225px;height:30px">Phone</div>
<div class="abs field" style="left:368px;top:630px;width:225px;height:30px">Subject</div>
<div class="abs field" style="left:123px;top:671px;width:470px;height:113px">Message</div>
<div class="abs submit display">SUBMIT</div>

<div class="abs map" role="img" aria-label="Street map showing the office location with a marker"></div>

<section class="abs info-card">
  <div class="abs info-col" style="left:0;width:272px">
    <div class="info-icon">
      <svg width="11" height="15" viewBox="0 0 11 15"><path d="M5.5 0A5.5 5.5 0 0 0 0 5.5C0 9.5 5.5 15 5.5 15S11 9.5 11 5.5A5.5 5.5 0 0 0 5.5 0z" fill="#8dc63f"/><circle cx="5.5" cy="5.5" r="2" fill="#f0f0f0"/></svg>
    </div>
    <div class="info-title">Our Office</div>
    <div class="info-text">123 euismod cidun ut laoreetmok<br>laoreet dol magnak aliquam</div>
  </div>
  <div class="abs col-rule" style="left:272px"></div>
  <div class="abs info-col" style="left:272px;width:280px">
    <div class="info-icon">
      <svg width="14" height="10" viewBox="0 0 14 10"><rect width="14" height="10" rx="1" fill="#8dc63f"/><path d="M0 1 7 6 14 1" stroke="#f0f0f0" fill="none" stroke-width="1.3"/></svg>
    </div>
    <div class="info-title">Email Address</div>
    <div class="info-btn">info@bustanfresh.com</div>
  </div>
  <div class="abs col-rule" style="left:552px"></div>
  <div class="abs info-col" style="left:552px;width:247px">
    <div class="info-icon">
      <svg width="14" height="14" viewBox="0 0 24 24"><path fill="#8dc63f" d="M6.6 10.8a15 15 0 0 0 6.6 6.6l2.2-2.2c.3-.3.7-.4 1-.2 1.1.4 2.3.6 3.6.6.6 0 1 .4 1 1V20c0 .6-.4 1-1 1A17 17 0 0 1 3 4c0-.6.4-1 1-1h3.5c.6 0 1 .4 1 1 0 1.3.2 2.5.6 3.6.1.3 0 .7-.2 1z"/></svg>
    </div>
    <div class="info-title">Contact No</div>
    <div class="info-btn">123 456 7890</div>
  </div>
</section>

<div class="abs social-foot" aria-label="Social links">
  <div class="social-dot"><span></span></div>
  <div class="social-dot"><span></span></div>
  <div class="social-dot"><span></span></div>
  <div class="social-dot"><span></span></div>
</div>

<footer class="abs footer-bar">
  Copyright © 2018 <span class="brand-inline">BUSTAN</span>. All Right Reserved.
</footer>

</body>
</html>
```